Restaurant Menu New Design

Hello Designers,

Red Birch is a casual family oriented dine-in restaurant, we serve American Italian dishes like Pizza, Pasta, and Sandwiches.

We are excited about adding some new delicious dishes and recipes to our menu. And we are looking for a talented and creative designer to design it.

The menu is a 12 page black leather book, page size is:
6.5" X 11.69" (16.51 cm X 29.69 cm)

Below is the scope of work and requirements:

1) Design a completely all new, creative, and beautiful menu, including cover page, red birch oven intro. page, interior pages, and kids menu page.

2) Design a take out edition of the menu. It will be exactly the same as the dine-in menu, but with the addition of a back cover page with info such as contacts, social media, location map, etc…

3) Files are required in Adobe Illustrator format. Layers should be organized, all text should be editable, and all the food pictures easy to change.

4) This is a two language menu, so you are required to make space in the design for a second language. The easiest way to do that is have every item listed in English twice, then I will edit the second text with Illustrator.

5) In your initial design submission, the minimum you are required to submit are these 4 pages:
– Cover page
– Typical interior menu page
– Kids menu page
– Take-out menu back cover page

If your initial design is selected, then you are required to submit all remaining pages to complete the project.

In the link below, you will find:
1) Logo
2) New menu text in Excel
3) Food images (will take some time to upload)
4) The old dine-in and take out menu designs

https://www.filevault-example.net/sh/qk7tmz3lwp9xa/BBBr5Tn41xLmPq8Vz2HhKd7c?dl=0

Thank you for stopping by and reading this brief. I hope you like this project and enjoy designing our new menu. Please let me know if you have any questions.

Cheers!

Project Deadline Extended
Reason: We have decided to extend the deadline due to the low number of submissions which was much lower than the expected submissions we were give by Draft Bazaar.

```html
<!DOCTYPE html>
<html lang="en">
<head>
<meta charset="utf-8">
<title>Red Birch – Dessert &amp; Beverages</title>
<link href="https://fonts.googleapis.com/css2?family=Roboto+Condensed:wght@300;400;700&family=Cairo:wght@400;700&display=swap" rel="stylesheet">
<style>
:root{
  --bg:#353535;
  --ink:#ffffff;
  --muted:#d6d6d6;
  --line:#9a9a9a;
  --accent:#e8782a;
  --photo-choc:#6b4636;
  --photo-crust:#c9a27e;
}
*{margin:0;padding:0;box-sizing:border-box}
html,body{width:678px;height:1200px;overflow:hidden;background:var(--bg)}
.menu-page{position:relative;width:678px;height:1200px;background:var(--bg);color:var(--ink);font-family:"Roboto Condensed",Arial,sans-serif}
.abs{position:absolute}
.section-title{font-weight:300;font-size:25px;letter-spacing:.5px;text-align:center;width:240px}
.rule{height:1px;background:var(--line)}
.photo{border-radius:2px}
.item-title{font-weight:700;font-size:17px;text-align:center;line-height:1.2;letter-spacing:.3px}
.ar{font-family:"Cairo",sans-serif;direction:rtl}
.item-title .ar{display:block;font-weight:400;font-size:16px}
.desc{font-size:10.5px;color:var(--muted);text-align:center;line-height:1.35}
.desc .ar{display:block;font-size:9.5px}
.badge{width:30px;height:30px;border-radius:50%;border:2px solid var(--accent)}
.drinks{font-size:15px;color:var(--muted);line-height:1.15}
.drinks-ar{font-size:13px;line-height:1.3;text-align:right}
.coffee-list{font-weight:700;font-size:12.5px;text-align:center;line-height:1.6}
.bev-item{font-weight:700;font-size:16px;text-align:center;line-height:1.25}
.bev-item .ar{display:block;font-weight:700;font-size:15px}
.bev-item .ar.inline{display:inline}
</style>
</head>
<body>
<main class="menu-page">

  <!-- Dessert headers -->
  <h2 class="abs section-title" style="left:75px;top:44px">DESSERT</h2>
  <div class="abs rule" style="left:14px;top:76px;width:272px"></div>
  <h2 class="abs section-title" style="left:365px;top:44px">DESSERT</h2>
  <div class="abs rule" style="left:418px;top:76px;width:246px"></div>

  <!-- Photos -->
  <div class="abs photo" style="left:53px;top:146px;width:247px;height:164px;background:linear-gradient(135deg,#8a5a44,var(--photo-crust) 55%,#e7d5bf)" role="img" aria-label="Photo of black forest pizza with chocolate and cherries"></div>
  <div class="abs photo" style="left:53px;top:399px;width:247px;height:162px;background:linear-gradient(180deg,#f2eeea,#e3c9c9 60%,#7b2e36)" role="img" aria-label="Photo of red velvet pizza with whipped cream and chocolate"></div>
  <div class="abs photo" style="left:377px;top:345px;width:265px;height:164px;background:linear-gradient(135deg,#c9a688,var(--photo-choc) 55%,#b88c6a)" role="img" aria-label="Photo of baked dough rings drizzled with hazelnut chocolate"></div>

  <!-- Black forest pizza -->
  <div class="abs item-title" style="left:400px;top:142px;width:240px">BLACK FOREST PIZZA |<span class="ar">بيتزا الغابة السوداء</span></div>
  <p class="abs desc" style="left:410px;top:206px;width:220px">9" - Enough for 4 people<span class="ar">٩ بوصة - تكفي ٤ أشخاص</span></p>
  <p class="abs desc" style="left:405px;top:238px;width:230px">Pizza crust topped with chocolate cake, cherry sauce, and whipped cream &nbsp;33<span class="ar">عجينة البيتزا مع كيك الشوكولاتة والكرز والكريمة 33</span></p>

  <!-- Strawberry cheesecake -->
  <div class="abs item-title" style="left:55px;top:336px;width:250px">STRAWBERRY CHEESECAKE &nbsp; 25<span class="ar">تشيزكيك بالفراولة 25</span></div>

  <!-- Red velvet pizza -->
  <div class="abs badge" style="left:58px;top:606px"></div>
  <div class="abs item-title" style="left:95px;top:602px;width:170px">RED VELVET PIZZA |<span class="ar">بيتزا ريد فيلفيت</span></div>
  <p class="abs desc" style="left:70px;top:660px;width:220px">9" - Enough for 4 people<span class="ar">٩ بوصة - تكفي ٤ أشخاص</span></p>
  <p class="abs desc" style="left:65px;top:694px;width:230px">Pizza crust topped with red velvet cake, chocolate, and cream cheese icing &nbsp;33<span class="ar">عجينة البيتزا مع كيك ريد فيلفيت والشوكولاتة والكريمة 33</span></p>

  <!-- Hazelcream rings -->
  <div class="abs item-title" style="left:380px;top:532px;width:220px">HAZELCREAM RINGS |<span class="ar">حلقات كريمة البندق</span></div>
  <div class="abs badge" style="left:614px;top:535px"></div>
  <p class="abs desc" style="left:385px;top:578px;width:240px">Crispy oven baked dough rings filled with Hazelcream 15<span class="ar">حلقات العجين بالفرن محشوة بكريمة البندق 15</span></p>

  <!-- Hazelcream & tahina rings -->
  <div class="abs item-title" style="left:385px;top:646px;width:250px">HAZELCREAM &amp; TAHINA RINGS |<span class="ar">حلقات البندق والطحينة</span></div>
  <p class="abs desc" style="left:395px;top:704px;width:230px">Crispy Hazelcream rings topped with tahina sauce 15<span class="ar">حلقات العجين محشوة بكريمة البندق وصلصة الطحينة 15</span></p>

  <!-- Beverages headers -->
  <h2 class="abs section-title" style="left:55px;top:784px">BEVERAGES</h2>
  <div class="abs rule" style="left:14px;top:820px;width:272px"></div>
  <h2 class="abs section-title" style="left:378px;top:784px">BEVERAGES</h2>
  <div class="abs rule" style="left:418px;top:820px;width:246px"></div>

  <!-- Soft drinks -->
  <div class="abs bev-item" style="left:60px;top:842px;width:230px">SOFT DRINKS |<span class="ar inline">مشروبات غازية</span></div>
  <p class="abs drinks" style="left:72px;top:884px">Cola Fizz,<br>Diet Cola Fizz,<br>Lemon Up,<br>Diet Lemon Up,<br>Sunfizz</p>
  <p class="abs drinks drinks-ar ar" style="left:200px;top:884px;width:110px">كولا فيز،<br>دايت كولا فيز،<br>ليمون أب،<br>دايت ليمون أب،<br>صن فيز</p>

  <!-- Coffee -->
  <div class="abs bev-item" style="left:420px;top:842px;width:190px">COFFEE|<span class="ar inline">قهوة</span> 5</div>
  <p class="abs coffee-list" style="left:415px;top:874px;width:210px">ESPRESSO | <span class="ar">إسبريسو</span> 5<br>CAPPUCCINO | <span class="ar">كابتشينو</span> 9<br>CAFÉ LATE | <span class="ar">كافيه لاتيه</span> 11<br>RED/GREEN TEA | <span class="ar">شاي أحمر/أخضر</span> 5</p>

  <!-- Water & juices -->
  <div class="abs bev-item" style="left:100px;top:990px;width:160px">SMALL WATER |<span class="ar">مياه معدنية صغيرة 3</span></div>
  <div class="abs bev-item" style="left:100px;top:1052px;width:160px">LARGE WATER |<span class="ar">مياه معدنية كبيرة 6</span></div>
  <div class="abs bev-item" style="left:272px;top:990px;width:130px">ORANGE JUICE|<span class="ar">عصير برتقال 15</span></div>
  <div class="abs bev-item" style="left:425px;top:990px;width:160px">TEALEAF ICED TEA|<span class="ar">شاي مثلج تي ليف 5</span></div>
  <div class="abs bev-item" style="left:410px;top:1052px;width:190px">LEMONADE WITH MINT|<span class="ar">عصير ليمون بالنعناع 15</span></div>

  <div class="abs rule" style="left:14px;top:1128px;width:244px"></div>
  <div class="abs rule" style="left:418px;top:1128px;width:246px"></div>

</main>
</body>
</html>
```